Boutique hotel requires flyer for Tapas promotion

We need a flyer that will predominantly be used as a Face book promotion and for our website.
We would like to promote the fact that we offer Tapas & open our wine bar from 5pm to 8pm every Friday. Great for after work drinks, parties, corporate events etc.
I have attached our logo that I would like incorporated.
Our website is www.tamberlow.com.au if you would like to get a feel for the property.

Hotel

```html
<!DOCTYPE html>
<html lang="en">
<head>
<meta charset="utf-8">
<title>The Tamberlow – Friday Tapas &amp; Wine Bar</title>
<link href="https://fonts.googleapis.com/css2?family=Courgette&display=swap" rel="stylesheet">
<style>
  :root {
    --paper: #ffffff;
    --frame-outer: #c9946a;
    --frame-inner: #a8714a;
    --brand: #b98454;
    --ink: #111111;
  }
  * { margin: 0; padding: 0; box-sizing: border-box; }
  html, body {
    width: 800px;
    height: 1200px;
    overflow: hidden;
    background: var(--paper);
  }
  .flyer {
    position: relative;
    width: 800px;
    height: 1200px;
    background: var(--paper);
  }
  .flyer-frame {
    position: absolute;
    inset: 0;
    width: 800px;
    height: 1200px;
  }
  .frame-outer { fill: var(--paper); stroke: var(--frame-outer); stroke-width: 10; }
  .frame-inner { fill: none; stroke: var(--frame-inner); stroke-width: 3; }
  .badge-outer { fill: var(--paper); stroke: var(--frame-outer); stroke-width: 6; }
  .badge-inner { fill: none; stroke: var(--frame-inner); stroke-width: 2; }

  .brand {
    position: absolute;
    left: 256px;
    top: 130px;
    width: 288px;
    height: 204px;
    display: flex;
    flex-direction: column;
    align-items: center;
    justify-content: center;
    gap: 20px;
  }
  .brand-mark {
    width: 30px;
    height: 30px;
    background: var(--brand);
  }
  .brand-name {
    font-family: "Courgette", cursive;
    font-size: 34px;
    font-weight: 400;
    color: var(--brand);
    line-height: 1;
    white-space: nowrap;
  }

  .announcement {
    position: absolute;
    left: 58px;
    top: 530px;
    width: 720px;
    font-family: "Courgette", cursive;
    font-size: 53px;
    line-height: 60px;
    color: var(--ink);
  }
</style>
</head>
<body>
  <main class="flyer">
    <svg class="flyer-frame" viewBox="0 0 800 1200" aria-hidden="true">
      <path class="frame-outer" d="M84 12 H716 A70 70 0 0 0 786 82 V1118 A70 70 0 0 0 716 1188 H84 A70 70 0 0 0 14 1118 V82 A70 70 0 0 0 84 12 Z"/>
      <path class="frame-inner" d="M88 28 H712 A58 58 0 0 0 770 86 V1114 A58 58 0 0 0 712 1172 H88 A58 58 0 0 0 30 1114 V86 A58 58 0 0 0 88 28 Z"/>
      <path class="badge-outer" d="M276 130 H524 A20 20 0 0 0 544 150 V314 A20 20 0 0 0 524 334 H276 A20 20 0 0 0 256 314 V150 A20 20 0 0 0 276 130 Z"/>
      <path class="badge-inner" d="M280 140 H520 A14 14 0 0 0 534 154 V310 A14 14 0 0 0 520 324 H280 A14 14 0 0 0 266 310 V154 A14 14 0 0 0 280 140 Z"/>
    </svg>

    <header class="brand">
      <span class="brand-mark"></span>
      <span class="brand-name">The Tamberlow</span>
    </header>

    <p class="announcement">We are happy to announce that we offer Tapas and open our wine bar from 5pm to 8 pm every Friday.</p>
  </main>
</body>
</html>
```